Pellbry Redesign of Website

I require my webpage to look different but this is out with my current providers platform
Updates
I will benefit from designs that use my wording (this is extremely important). I appreciate there may be a lot of wording in some areas so i would be happy with "read more" in various places. The use of my face in photo is a must and my logo is also a must which can be found on m y website www.pellbryfocus.co.uk I do not want corporate feel, i would like a warm, authentic. personal and inviting feel.
5+ page

```html
<!DOCTYPE html>
<html lang="en">
<head>
<meta charset="utf-8">
<title>The Story Behind Pellbry</title>
<link rel="stylesheet" href="https://fonts.googleapis.com/css2?family=Alegreya:ital,wght@0,400;0,500;0,600;1,400;1,500&family=Montserrat:wght@400;500;600&display=swap">
<style>
:root{
  --ink:#123c38;
  --ink-deep:#0f3531;
  --text:#222a2a;
  --gold:#a8873a;
  --paper:#f8f6f2;
  --sand:#f3eee6;
  --line:#e3ddd3;
  --chip-beige:#e5dcc6;
  --chip-grey:#cfd4dc;
  --teal-soft:#6f9a9b;
}
*{box-sizing:border-box;margin:0;padding:0}
html,body{width:1200px;height:3315px;overflow:hidden}
body{background:var(--paper);font-family:"Montserrat",sans-serif;color:var(--text);position:relative}

/* hero */
.hero{position:absolute;left:0;top:0;width:1200px;height:532px}
.hero-bg{position:absolute;left:0;top:0;width:1200px;height:778px;background:var(--sand)}
.hero-photo{position:absolute;right:0;top:0;width:760px;height:532px;
  background:linear-gradient(90deg,rgba(243,238,230,1) 0%,rgba(243,238,230,0) 30%),
  linear-gradient(180deg,#d3dde4 0%,#b6c8d4 32%,#8fa86e 58%,#7d9c86 78%,#4f6b52 100%)}
.menu{position:absolute;left:110px;top:72px;width:32px}
.menu span{display:block;height:3px;background:var(--ink);border-radius:2px;margin-bottom:6px}
.menu span:nth-child(2){width:26px}
.brand{position:absolute;left:160px;top:60px;display:flex;align-items:center;gap:10px}
.brand-dot{width:40px;height:40px;border-radius:50%;background:var(--teal-soft)}
.brand-name{font-family:"Alegreya",serif;font-size:15px;font-weight:500;color:var(--teal-soft);letter-spacing:.06em;text-transform:uppercase}
.hero h1{position:absolute;left:110px;top:194px;font-family:"Alegreya",serif;font-weight:500;font-size:86px;line-height:84px;color:var(--ink)}
.rule{height:2px;background:linear-gradient(90deg,var(--gold),rgba(168,135,58,0))}
.hero .rule{position:absolute;left:110px;top:376px;width:240px}
.hero .tagline{position:absolute;left:110px;top:392px;font-family:"Alegreya",serif;font-style:italic;font-size:24px;color:var(--ink)}
.btn{display:inline-block;font-family:"Alegreya",serif;font-weight:600;color:#fff;background:var(--ink-deep);border-radius:22px;font-size:16px}
.hero .btn{position:absolute;left:111px;top:439px;padding:10px 22px}

/* bio */
.bio{position:absolute;left:110px;top:533px;width:1090px;height:488px;background:var(--sand);border:1px solid var(--line);border-right:none;border-radius:12px 0 0 12px}
.bio-mark{position:absolute;left:38px;top:38px;width:124px;height:124px;border-radius:50%;background:var(--ink-deep)}
.bio-body{position:absolute;left:196px;top:22px;width:790px}
.bio h2{font-family:"Alegreya",serif;font-weight:500;font-size:31px;color:var(--ink)}
.bio .role{font-family:"Alegreya",serif;font-style:italic;font-weight:500;font-size:18px;color:var(--ink);margin-top:2px}
.bio .lead{font-weight:600;font-size:14px;color:#111;margin-top:8px}
.bio-text{border-left:2px solid #7a7a7a;padding-left:14px;margin-top:6px;font-size:13px;line-height:23px}
.bio-text p+p{margin-top:23px}

/* story columns */
.story{position:absolute;top:1068px;left:110px;width:978px;display:flex;gap:50px}
.story-card{flex:1;height:774px;border:1px solid var(--line);border-radius:12px;background:#f7f5f1;padding:20px 20px 0}
.story-card h3{font-family:"Alegreya",serif;font-weight:500;font-size:30px;line-height:36px;color:var(--ink)}
.story-card .rule{width:240px;margin:16px 0 20px}
.point{display:flex;gap:14px;align-items:center;margin-bottom:9px}
.point p{font-size:12.5px;line-height:23px;max-width:360px}
.chip{flex:none;width:54px;height:54px;border-radius:50%;background:var(--chip-beige);display:flex;align-items:center;justify-content:center}
.chip.grey{background:var(--chip-grey)}
.chip svg{width:26px;height:26px;stroke:#3d4f5a;fill:none;stroke-width:1.6}

/* approach */
.approach{position:absolute;top:1880px;left:0;width:1200px;text-align:center}
.section-title{font-family:"Alegreya",serif;font-weight:500;font-size:42px;color:var(--ink)}
.center-rule{width:120px;height:2px;margin:12px auto 0;background:linear-gradient(90deg,rgba(168,135,58,0),var(--gold),rgba(168,135,58,0))}
.approach .intro{font-size:15px;margin-top:28px}
.values{display:flex;justify-content:center;margin:24px auto 0;width:1010px}
.value{width:126px;text-align:center;font-size:14px;line-height:21px;padding:0 6px}
.value .chip{width:72px;height:72px;margin:0 auto 8px}
.approach .note{font-family:"Alegreya",serif;font-size:22px;color:var(--gold);margin-top:34px}

/* qualifications */
.quals{position:absolute;top:2268px;left:0;width:1200px;text-align:center}
.qual-row{display:flex;gap:27px;justify-content:center;margin-top:38px}
.qual{width:308px;height:191px;border:1px solid var(--line);border-radius:10px;background:#f8f6f2;display:flex;flex-direction:column;align-items:center;justify-content:flex-end;padding-bottom:28px}
.badge{width:84px;height:84px;border-radius:50%;margin-bottom:22px}
.badge.wide{width:150px;height:60px;border-radius:8px;margin-bottom:34px;background:#c9d3de}
.badge.ring{background:#e4dcc2;border:3px solid #2a4c8a}
.badge.solid{background:#1d4d7a}
.qual .name{font-size:18px;font-weight:500;color:#111}

/* cta */
.cta{position:absolute;top:2596px;left:141px;width:919px;height:129px;background:var(--ink-deep);border-radius:10px}
.cta-ring{position:absolute;left:38px;top:24px;width:82px;height:82px;border:1px solid #6e8580;border-radius:50%;display:flex;align-items:center;justify-content:center}
.cta-ring svg{width:42px;height:42px;stroke:var(--gold);fill:none;stroke-width:2}
.cta h4{position:absolute;left:145px;top:20px;font-weight:500;font-size:25px;color:#fff}
.cta .btn{position:absolute;left:146px;top:62px;background:var(--gold);padding:9px 18px;font-size:15px}

/* footer */
.footer{position:absolute;top:2790px;left:0;width:1200px;height:525px;text-align:center}
.foot-scene{position:absolute;left:0;bottom:0;width:1200px;height:290px;
  background:linear-gradient(180deg,rgba(248,246,242,1) 0%,rgba(205,200,205,.8) 18%,#9a8f9c 40%,#d58a5a 62%,#6b5660 82%,#3e3341 100%)}
.foot-content{position:relative;z-index:1}
.foot-brand{display:flex;flex-direction:column;align-items:center;gap:14px}
.foot-brand .brand-dot{width:110px;height:110px}
.foot-links{display:flex;justify-content:center;gap:72px;margin-top:46px;font-size:16px;font-weight:500;color:#111}
.copy{font-size:15px;margin-top:28px;color:#111}
</style>
</head>
<body>

<header class="hero">
  <div class="hero-bg"></div>
  <div class="hero-photo" role="img" aria-label="Photo of the founder smiling in front of a mountain river valley"></div>
  <div class="menu"><span></span><span></span><span></span></div>
  <div class="brand"><span class="brand-dot"></span><span class="brand-name">Pellbry</span></div>
  <h1>The Story<br>Behind Pellbry</h1>
  <div class="rule"></div>
  <p class="tagline">Helping others begin with understanding myself.</p>
  <a class="btn">Get Started</a>
</header>

<section class="bio">
  <div class="bio-mark"></div>
  <div class="bio-body">
    <h2>My name is ELSPETH MORAY CRANE,</h2>
    <p class="role">Founder of Pellbry.</p>
    <p class="lead">Pellbry was created from both lived experience and professional expertise.</p>
    <div class="bio-text">
      <p>My adult ADHD diagnosis came during a period of profound self-discovery following a mental health breakdown. While studying Integrative Counselling at the University of the Northern Isles, I began to understand myself in ways I never had before.</p>
      <p>For many years, my ADHD had gone unrecognised, and I was treated only with antidepressants, which never addressed the underlying cause of my struggles. Learning about ADHD didn't cause my breakdown—it helped explain it. It gave me the answers I had been searching for and marked the beginning of a journey towards greater self-understanding and self-compassion.</p>
      <p>As my understanding grew, I also recognised that I am autistic, something that is common alongside ADHD. Research suggests that ADHD and autism overlap in around 50–70% of cases, and many adults only recognise the second neurotype once the first has been identified. Although not a clinical diagnosis, many people refer to this combined experience as AuDHD. For me, it brought even greater clarity and helped me understand both my strengths and the challenges I had experienced throughout life.</p>
    </div>
  </div>
</section>

<section class="story">
  <article class="story-card">
    <h3>As a woman navigating both ADHD and perimenopause,</h3>
    <div class="rule"></div>
    <div class="point"><span class="chip"><svg viewBox="0 0 26 26"><circle cx="13" cy="13" r="4"/><circle cx="5" cy="6" r="2"/><circle cx="21" cy="6" r="2"/><circle cx="13" cy="22" r="2"/></svg></span><p>I have also experienced first-hand how hormonal changes can make neurodivergent traits more noticeable and difficult to manage.</p></div>
    <div class="point"><span class="chip grey"><svg viewBox="0 0 26 26"><circle cx="13" cy="13" r="10"/><circle cx="13" cy="13" r="6"/><circle cx="13" cy="13" r="2"/></svg></span><p>For many women, perimenopause is the stage of life where ADHD traits become more apparent, or previously successful coping strategies suddenly stop working.</p></div>
    <div class="point"><span class="chip"><svg viewBox="0 0 26 26"><circle cx="13" cy="7" r="3"/><path d="M6 22c1-6 13-6 14 0"/></svg></span><p>Understanding these connections strengthened my passion for helping neurodivergent individuals better understand their brains, develop self-compassion and discover practical strategies that genuinely support their wellbeing.</p></div>
    <div class="point"><span class="chip grey"><svg viewBox="0 0 26 26"><path d="M13 3a7 7 0 0 0-4 13v3h8v-3a7 7 0 0 0-4-13z"/><path d="M10 23h6"/></svg></span><p>This personal journey inspired me to deepen my professional knowledge. I completed a Higher National Qualification in Integrative Counselling, gaining valuable self-awareness alongside practical and theoretical skills.</p></div>
    <div class="point"><span class="chip"><svg viewBox="0 0 26 26"><path d="M13 21s-8-5-8-10a4 4 0 0 1 8-1 4 4 0 0 1 8 1c0 5-8 10-8 10z"/></svg></span><p>While I chose not to continue into the final year, I realised my passion lay in offering a more holistic approach—one that went beyond simply providing a listening ear.</p></div>
    <div class="point"><span class="chip grey"><svg viewBox="0 0 26 26"><circle cx="8" cy="9" r="3"/><circle cx="18" cy="9" r="3"/><path d="M3 21c1-5 9-5 10 0M13 21c1-5 9-5 10 0"/></svg></span><p>I wanted to empower people with practical knowledge, strategies and tools that they could continue using long after our work together had ended.</p></div>
  </article>
  <article class="story-card">
    <h3>I therefore qualified as a Health and Wellbeing Coach through Open Ridge Academy,</h3>
    <div class="rule"></div>
    <div class="point"><span class="chip grey"><svg viewBox="0 0 26 26"><rect x="5" y="5" width="16" height="14" rx="1"/><path d="M3 21h20"/></svg></span><p>A nationally recognised training provider, before completing additional specialist training in Autism, ADHD and Somatic Coaching.</p></div>
    <div class="point"><span class="chip"><svg viewBox="0 0 26 26"><rect x="4" y="4" width="12" height="9"/><circle cx="19" cy="15" r="3"/><path d="M14 23c1-4 9-4 10 0"/></svg></span><p>Somatic coaching explores the connection between the mind, body and nervous system, helping clients recognise how stress and emotions are held within the body while developing practical regulation strategies that can be particularly beneficial for neurodivergent individuals.</p></div>
    <div class="point"><span class="chip grey"><svg viewBox="0 0 26 26"><rect x="6" y="8" width="14" height="13"/><circle cx="13" cy="5" r="2"/></svg></span><p>I believe learning never stops, and I continue to undertake professional development in neurodiversity, wellbeing and mental health to ensure my knowledge and practice continue to evolve.</p></div>
    <div class="point"><span class="chip"><svg viewBox="0 0 26 26"><circle cx="13" cy="13" r="8"/><circle cx="13" cy="13" r="3"/></svg></span><p>Alongside my professional training, I am also a mother to three neurodivergent children with different diagnoses.</p></div>
    <div class="point"><span class="chip grey"><svg viewBox="0 0 26 26"><circle cx="13" cy="13" r="9"/><path d="M4 13h18M13 4v18"/></svg></span><p>This has given me invaluable lived experience of advocating for my children, navigating education and healthcare systems, creating a calmer home environment and understanding the everyday realities that many neurodivergent families face.</p></div>
    <div class="point"><span class="chip"><svg viewBox="0 0 26 26"><circle cx="13" cy="6" r="2.5"/><circle cx="6" cy="18" r="2.5"/><circle cx="20" cy="18" r="2.5"/><path d="M13 9v5M13 14l-6 2M13 14l6 2"/></svg></span><p>Together, my personal experiences and professional qualifications shape the compassionate, neuro-affirming approach that sits at the heart of everything I do.</p></div>
  </article>
</section>

<section class="approach">
  <h2 class="section-title">The Pellbry Approach</h2>
  <div class="center-rule"></div>
  <p class="intro">Everything I offer through Pellbry has been chosen with purpose.</p>
  <div class="values">
    <div class="value"><span class="chip"><svg viewBox="0 0 26 26"><path d="M4 14l5-5 4 4 4-4 5 5-9 8z"/></svg></span>Purpose-Driven Support</div>
    <div class="value"><span class="chip grey"><svg viewBox="0 0 26 26"><circle cx="13" cy="10" r="4"/><path d="M5 22c1-6 15-6 16 0"/></svg></span>Lived Experience</div>
    <div class="value"><span class="chip"><svg viewBox="0 0 26 26"><circle cx="13" cy="13" r="9"/><path d="M9 14c2 3 6 3 8 0"/></svg></span>Proven in Everyday Life</div>
    <div class="value"><span class="chip grey"><svg viewBox="0 0 26 26"><circle cx="13" cy="10" r="4"/><path d="M5 22c1-6 15-6 16 0"/></svg></span>Individual-Centred Approach</div>
    <div class="value"><span class="chip"><svg viewBox="0 0 26 26"><path d="M6 6v14M20 6v14M6 13h14"/></svg></span>No One-Size-Fits-All</div>
    <div class="value"><span class="chip grey"><svg viewBox="0 0 26 26"><rect x="6" y="4" width="14" height="18" rx="1"/><path d="M9 9h8M9 13h8M9 17h5"/></svg></span>Practical &amp; Sustainable Strategies</div>
    <div class="value"><span class="chip"><svg viewBox="0 0 26 26"><path d="M3 14l6-5 4 3 4-3 6 5-10 7z"/></svg></span>Building Confidence &amp; Wellbeing</div>
    <div class="value"><span class="chip grey"><svg viewBox="0 0 26 26"><circle cx="13" cy="13" r="9"/><path d="M9 11h8M9 15h8"/></svg></span>Compassionate Neurodiversity-Affirming Care</div>
  </div>
  <p class="note">Because sometimes the smallest changes can make the biggest difference.</p>
</section>

<section class="quals">
  <h2 class="section-title">Coaching Qualifications</h2>
  <div class="center-rule"></div>
  <div class="qual-row">
    <div class="qual"><span class="badge wide"></span><span class="name">Open Ridge Academy</span></div>
    <div class="qual"><span class="badge ring"></span><span class="name">The Coaching Standards Guild</span></div>
    <div class="qual"><span class="badge solid"></span><span class="name">Tailored Care College</span></div>
  </div>
</section>

<section class="cta">
  <div class="cta-ring"><svg viewBox="0 0 42 42"><path d="M21 34s-13-8-13-17a7 7 0 0 1 13-3 7 7 0 0 1 13 3c0 9-13 17-13 17z"/></svg></div>
  <h4>Discover your inner strength and cultivate a balanced life</h4>
  <a class="btn">Contact Pellbry</a>
</section>

<footer class="footer">
  <div class="foot-scene" role="img" aria-label="Photo of snowy mountain peaks at sunrise"></div>
  <div class="foot-content">
    <div class="foot-brand"><span class="brand-dot"></span><span class="brand-name">Pellbry</span></div>
    <nav class="foot-links"><span>Privacy Policy</span><span>Support Links</span><span>Terms &amp; Conditions</span></nav>
    <p class="copy">Copyrights@2026.Pellbry ADHD Coaching and Wellbeing.All Rights Reserved</p>
  </div>
</footer>

</body>
</html>
```